Hiking Made Simple Outfitter Directory

Hero Section
Image: A serene and picturesque camping landscape with a lake, mountains, and a few trees There is a circle of people sitting around a campfire. The image should be high-quality and visually appealing.
Headline: "Introducing Hikingmadesimple.net's Outfitter Directory"
Subheading: "Join our directory of trusted outfitters and reach a targeted audience of camping enthusiasts."
Call-to-Action (CTA) Button: "Learn More" or "Join Now"
Color scheme: Match hikingmadesimple.net and the logo
Example:
[Image: A serene and picturesque camping landscape with a lake, mountains, and a few trees]
Introducing Hikingmadesimple.net's Outfitter Directory
Join our directory of trusted outfitters and reach a targeted audience of camping enthusiasts.
Learn More
Benefits Section
Image: A group of happy campers sitting around a campfire, roasting marshmallows and telling stories.
Headline: "Benefits of Joining Our Directory"
Bullet points:
"Increase your exposure and visibility to potential customers"
"Book more trips and generate more revenue"
"Access a targeted audience of camping enthusiasts"
Color scheme: match hikingmadesimple.net
Example:
[Image: A group of happy campers sitting around a campfire, roasting marshmallows and telling stories]
Benefits of Joining Our Directory
• Increase your exposure and visibility to potential customers • Book more trips and generate more revenue • Access a targeted audience of camping enthusiasts
Features Section
Image: A screenshot of the directory's search functionality, showing a list of outfitters with their logos, names, and locations.
Headline: "Features of Our Outfitter Directory"
Bullet points:
"Search functionality to find outfitters by location, activity, or type"
"Outfitter profiles with detailed information and reviews"
"Booking system to make it easy for customers to book trips"
Example:
[Image: A screenshot of the directory's search functionality, showing a list of outfitters with their logos, names, and locations]
Features of Our Outfitter Directory
• Search functionality to find outfitters by location, activity, or type • Outfitter profiles with detailed information and reviews • Booking system to make it easy for customers to book trips
CTA Section
Image: A simple and clean design with a prominent call-to-action button.
Headline: "Express Interest in Joining Our Directory"
Call-to-Action (CTA) Button: "Express Interest" or "Join Now"

Example:
[Image: A simple and clean design with a prominent call-to-action button]
Express Interest in Joining Our Directory
Express Interest
Contact Information Section
Image: A simple and clean design with a form to collect contact information.
Headline: "Get in Touch with Us"
Form fields:
Name
Email
Phone
Website

```html
<!DOCTYPE html>
<html lang="en">
<head>
<meta charset="UTF-8">
<title>Hiking Made Simple — Outfitter Directory</title>
<link href="https://fonts.googleapis.com/css2?family=Oswald:wght@500;600;700&family=Inter:wght@400;500;600;700&display=swap" rel="stylesheet">
<style>
:root{
  --navy:#14264a;
  --navy-deep:#1f2a4d;
  --teal:#16a0a6;
  --orange:#f5a11f;
  --orange-red:#f0531d;
  --red:#e5262a;
  --cream:#fdf2d2;
  --sun:#fee591;
  --sun-deep:#fbc02c;
  --white:#ffffff;
  --text:#1e2533;
  --muted:#6b7280;
  --line:#b9bec8;
}
*{margin:0;padding:0;box-sizing:border-box}
html,body{width:1200px;height:3618px;overflow:hidden}
body{position:relative;font-family:"Inter",Arial,sans-serif;color:var(--text);background:var(--white)}
.abs{position:absolute}
.display{font-family:"Oswald","Arial Narrow",sans-serif;font-weight:700;text-transform:uppercase;letter-spacing:.2px}
.btn{position:absolute;display:flex;align-items:center;justify-content:center;border-radius:4px;font-size:14px;font-weight:500;color:var(--white)}
.btn-orange{background:var(--orange)}
.btn-teal{background:var(--teal)}

/* hero */
.hero{position:absolute;left:0;top:0;width:1200px;height:744px;overflow:hidden;
  background:radial-gradient(ellipse 260px 200px at 320px 520px,rgba(245,140,40,.85),rgba(120,60,20,.3) 60%,transparent 80%),
  radial-gradient(ellipse 320px 380px at 860px 360px,rgba(150,110,80,.55),transparent 75%),
  linear-gradient(180deg,#3a3a2c 0%,#2e3224 40%,#3b3a28 75%,#2b2a1e 100%)}
.hero-edge{position:absolute;left:0;bottom:0}
.brand{position:absolute;display:flex;align-items:center;gap:10px;color:var(--white);font-weight:700;font-size:15px}
.brand-dot{width:40px;height:40px;border-radius:50%;background:var(--orange);flex:none}
.nav{position:absolute;top:50px;left:409px;display:flex;gap:37px;font-size:14px;color:var(--white)}
.nav .active{font-weight:600}
.nav .active::before{content:"";display:inline-block;width:4px;height:4px;border-radius:50%;background:#fff;margin-right:8px;vertical-align:middle}
.btn-outline{background:var(--white);color:var(--orange-red);border:1px solid var(--orange-red)}
.hero h1{position:absolute;left:100px;top:160px;font-size:57px;line-height:61px;color:var(--white)}
.hero p{position:absolute;left:100px;top:364px;width:520px;font-size:20px;line-height:30px;color:#eef0ec}

/* benefits */
.section-title{position:absolute;left:0;width:1200px;text-align:center;font-size:46px;color:var(--navy)}
.benefit-img{position:absolute;top:908px;width:292px;height:250px}
.benefit-text{position:absolute;top:1174px;width:292px;text-align:center;font-size:15px;line-height:23px;color:var(--navy)}

/* features band */
.features{position:absolute;left:0;top:1329px;width:1200px;height:365px;
  background:linear-gradient(90deg,#2a2b58 0%,#6b2548 22%,#4a2850 45%,#2c2a55 65%,#252a50 100%)}
.features h2{position:absolute;left:559px;top:44px;font-size:52px;line-height:54px;color:var(--white)}
.features h3{position:absolute;left:559px;top:164px;font-family:"Oswald",sans-serif;font-weight:600;font-size:23px;text-transform:uppercase;color:var(--white)}
.features p{position:absolute;left:559px;top:203px;width:420px;font-size:17px;line-height:25px;color:var(--white)}
.chip{position:absolute;top:245px;height:38px;border-radius:19px;display:flex;align-items:center;justify-content:center;gap:6px;font-size:12px;font-weight:500;color:var(--navy);border:2px solid #fff}
.search{position:absolute;left:110px;top:298px;width:357px;height:44px;border-radius:22px;background:#fff;border:1px solid #ddd}
.search span{position:absolute;left:16px;top:11px;font-size:17px;color:#8a8f98}
.search i{position:absolute;right:0;top:0;width:44px;height:44px;border-radius:50%;background:var(--orange-red)}

/* cream */
.cream{position:absolute;left:0;top:1694px;width:1200px;height:640px;background:var(--cream)}
.card{position:absolute;top:60px;width:482px;height:281px;background:#fff;border:1px solid #e3dccb;border-radius:10px;box-shadow:0 4px 16px rgba(0,0,0,.06)}
.label{position:absolute;font-size:13px;font-weight:700;color:var(--navy)}
.thumb{position:absolute;width:71px;height:49px;border-radius:2px}
.thumb-sm{width:86px;height:50px}
.feat-title{position:absolute;top:372px;font-family:"Oswald",sans-serif;font-weight:600;font-size:21px;text-transform:uppercase;color:var(--navy)}
.feat-text{position:absolute;top:408px;width:340px;font-size:15px;line-height:23px;color:#4b5563}

/* cta */
.cta{position:absolute;left:0;top:2334px;width:1200px;height:328px;background:var(--sun);overflow:hidden}
.cta h2{position:absolute;left:0;top:50px;width:1200px;text-align:center;font-size:48px;color:var(--orange-red)}
.cta p{position:absolute;left:0;top:116px;width:1200px;text-align:center;font-size:20px;line-height:26px;color:var(--orange-red)}
.stripe{position:absolute;left:0;width:1200px}

/* contact */
.field{position:absolute;height:49px;border:1px solid var(--line);background:#fff;font-size:15px;color:#333;padding:15px 20px}
.submit{position:absolute;left:261px;top:3086px;width:705px;height:54px;background:var(--orange);color:#fff;font-weight:600;font-size:16px;display:flex;align-items:center;justify-content:center;border-radius:2px}

/* footer */
.footer{position:absolute;left:0;top:3235px;width:1200px;height:383px;background:linear-gradient(180deg,#1f2b50 0%,#1e2a4d 70%,#22305a 100%);color:#fff}
.foot-h{position:absolute;top:62px;font-family:"Oswald",sans-serif;font-weight:600;font-size:16px;text-transform:uppercase}
.foot-list{position:absolute;top:98px;list-style:none;font-size:13px;line-height:31px}
.social{position:absolute;top:256px;width:21px;height:21px;border-radius:50%;border:2px solid #fff}
</style>
</head>
<body>

<!-- HERO -->
<section class="hero">
  <div class="abs" role="img" aria-label="Friends playing guitar by a campfire in a forest clearing beside a tent, with a dog lying nearby" style="inset:0"></div>
  <div class="brand" style="left:94px;top:38px"><span class="brand-dot"></span>Hiking Made Simple</div>
  <nav class="nav">
    <span class="active">Home</span><span>Campgrounds</span><span>Activities</span><span>Pricing</span>
  </nav>
  <a class="btn btn-teal" style="left:849px;top:41px;width:112px;height:36px">Join Now</a>
  <a class="btn btn-outline" style="left:975px;top:41px;width:113px;height:36px">Learn More</a>
  <h1 class="display">Introducing<br>Hikingmadesimple.net's<br>Outfitter Directory</h1>
  <p>Join our directory of trusted outfitters and reach a targeted audience of camping enthusiasts.</p>
  <a class="btn btn-orange" style="left:100px;top:446px;width:133px;height:46px">Join Now</a>
  <a class="btn btn-teal" style="left:251px;top:446px;width:133px;height:46px">Learn More</a>
  <svg class="hero-edge" width="1200" height="90" viewBox="0 0 1200 90">
    <path d="M0 90 L0 70 C80 60 130 40 200 62 C260 40 320 30 400 58 C470 38 560 30 640 60 C720 40 820 30 900 56 C980 36 1080 40 1160 62 L1200 70 L1200 90 Z" fill="#fff"/>
  </svg>
</section>

<!-- BENEFITS -->
<h2 class="section-title display" style="top:820px">Benefits of Joining Our Directory</h2>
<div class="benefit-img" role="img" aria-label="Group of friends roasting marshmallows around a campfire" style="left:100px;background:linear-gradient(160deg,#5a4a3a,#8a6a4a 50%,#3b3a35)"></div>
<div class="benefit-img" role="img" aria-label="Woman holding a fan of banknotes on a yellow background" style="left:453px;background:linear-gradient(160deg,#fdb813,#ffc21a 60%,#f1e6cf)"></div>
<div class="benefit-img" role="img" aria-label="Family at a campsite picnic table with camping chairs" style="left:808px;background:linear-gradient(170deg,#6d8a4a,#8da55e 45%,#6b5a44)"></div>
<p class="benefit-text" style="left:100px">Increase your exposure and visibility to potential customers</p>
<p class="benefit-text" style="left:453px">Book more trips and generate<br>more revenue</p>
<p class="benefit-text" style="left:808px">Access a targeted audience<br>of camping enthusiasts</p>

<!-- FEATURES -->
<section class="features">
  <svg class="abs" style="left:52px;top:0" width="480" height="365" viewBox="0 0 480 365" role="img" aria-label="Children playing outside a tent at a campsite">
    <defs><linearGradient id="tentPhoto" x1="0" y1="0" x2="0" y2="1">
      <stop offset="0" stop-color="#8aa25a"/><stop offset=".5" stop-color="#c7c3b5"/><stop offset="1" stop-color="#7e8a55"/></linearGradient></defs>
    <path d="M138 0 L342 0 C330 90 360 170 410 200 C380 240 350 300 345 365 L140 365 C120 300 60 250 0 240 C60 200 140 160 138 0 Z" fill="url(#tentPhoto)"/>
  </svg>
  <div class="chip" style="left:115px;width:96px;background:#bfe9e2">
    <svg width="12" height="12" viewBox="0 0 12 12"><circle cx="7" cy="2" r="1.6" fill="#14264a"/><path d="M6 4 L4 8 L2 11 M6 4 L8 7 L10 8 M5 6 L7 11" stroke="#14264a" stroke-width="1.4" fill="none"/></svg>Activity ˅</div>
  <div class="chip" style="left:230px;width:107px;background:#f8b59c">
    <svg width="11" height="13" viewBox="0 0 11 13"><path d="M5.5 12 C2 8 1 6 1 4.5 A4.5 4.5 0 0 1 10 4.5 C10 6 9 8 5.5 12 Z" fill="#14264a"/><circle cx="5.5" cy="4.5" r="1.6" fill="#f8b59c"/></svg>Location ˅</div>
  <div class="chip" style="left:356px;width:113px;background:#4dc56c">
    <svg width="11" height="11" viewBox="0 0 11 11" fill="#14264a"><rect width="4.5" height="4.5"/><rect x="6.5" width="4.5" height="4.5"/><rect y="6.5" width="4.5" height="4.5"/><rect x="6.5" y="6.5" width="4.5" height="4.5"/></svg>Type ˅</div>
  <div class="search"><span>Search</span><i>
    <svg width="44" height="44" viewBox="0 0 44 44"><circle cx="21" cy="21" r="6" stroke="#fff" stroke-width="2" fill="none"/><path d="M25.5 25.5 L29 29" stroke="#fff" stroke-width="2"/></svg></i></div>
  <h2 class="display">Features of Our<br>Outfitter Directory</h2>
  <h3>Features of Our Outfitter Directory</h3>
  <p>Our directory features a powerful search function that enables users to find outfitters based on criteria such as location, activity type (e.g., hiking, fishing, kayaking), and specific services (e.g., guided tours, equipment rentals).</p>
</section>

<!-- PROFILES & BOOKING -->
<section class="cream">
  <div class="card" style="left:100px">
    <div class="abs" role="img" aria-label="Outfitter group photo" style="left:34px;top:44px;width:88px;height:88px;border-radius:50%;background:linear-gradient(150deg,#c79a72,#8b6b4f)"></div>
    <div class="abs" style="left:143px;top:24px;display:flex">
      <span style="width:14px;height:14px;border-radius:50%;background:#b07a5a;border:1px solid #fff"></span>
      <span style="width:14px;height:14px;border-radius:50%;background:#6b7f9a;border:1px solid #fff;margin-left:-5px"></span>
      <span style="width:14px;height:14px;border-radius:50%;background:#d9a46a;border:1px solid #fff;margin-left:-5px"></span>
      <span style="width:14px;height:14px;border-radius:50%;background:#7d6a8b;border:1px solid #fff;margin-left:-5px"></span>
      <span style="font-size:8px;color:#555;margin-left:6px;line-height:14px">14+ Members</span>
    </div>
    <div class="abs" style="left:143px;top:50px;font-size:16px;font-weight:700;color:var(--navy)">Ridgeline Trail Outfitters</div>
    <div class="abs" style="left:143px;top:75px;width:230px;font-size:11px;line-height:16px;color:var(--muted)">Ridgeline Trail Outfitters specializes in guided hiking and camping experiences...</div>
    <div class="abs" style="left:143px;top:128px;display:flex;align-items:center;gap:4px;font-size:10px;font-weight:600;color:#333">
      <span style="color:#f5b400;font-size:17px;letter-spacing:3px">★★★★</span><span style="color:#cfcfcf;font-size:17px">★</span><span style="margin-left:6px">4.5/5.0</span></div>
    <div class="label" style="left:34px;top:166px">Service Offered</div>
    <div class="thumb" role="img" aria-label="Hiker on a snowy trail" style="left:34px;top:193px;background:linear-gradient(160deg,#a9b8cc,#6f7f96)"></div>
    <div class="thumb" role="img" aria-label="Campers around a tent" style="left:121px;top:193px;background:linear-gradient(160deg,#e0b94a,#6b7a3a)"></div>
    <div class="thumb" role="img" aria-label="Lion in the grass" style="left:208px;top:193px;background:linear-gradient(160deg,#d9a55a,#8b6030)"></div>
  </div>
  <div class="card" style="left:617px">
    <div class="label" style="left:16px;top:28px">Service Offered</div>
    <div class="thumb thumb-sm" role="img" aria-label="Hiker on a snowy trail" style="left:16px;top:54px;background:linear-gradient(160deg,#b8c6d8,#6f7f96)"></div>
    <div class="thumb thumb-sm" role="img" aria-label="Campers around a tent" style="left:120px;top:54px;background:linear-gradient(160deg,#e0b94a,#6b7a3a)"></div>
    <div class="thumb thumb-sm" role="img" aria-label="Tent under trees at night" style="left:224px;top:54px;background:linear-gradient(160deg,#3f4a45,#1e2624)"></div>
    <div class="thumb thumb-sm" role="img" aria-label="Forest trail" style="left:328px;top:54px;background:linear-gradient(160deg,#5a5348,#2d2a25)"></div>
    <div class="thumb thumb-sm" role="img" aria-label="Campfire at dusk" style="left:16px;top:120px;background:linear-gradient(160deg,#d97a3a,#3a2a20)"></div>
    <div class="thumb thumb-sm" role="img" aria-label="Camper van in a green field" style="left:120px;top:120px;background:linear-gradient(160deg,#9ab07a,#5e7a4a)"></div>
    <div class="thumb thumb-sm" role="img" aria-label="Friends by a fire" style="left:224px;top:120px;background:linear-gradient(160deg,#b9884a,#5a3a22)"></div>
    <div class="thumb thumb-sm" role="img" aria-label="Travel poster with a traveller" style="left:328px;top:120px;background:linear-gradient(160deg,#f0e3d8,#d4503a)"></div>
    <div class="thumb thumb-sm" role="img" aria-label="Mountain landscape" style="left:16px;top:186px;background:linear-gradient(180deg,#c9d4e0,#9a7a5a)"></div>
    <div class="thumb thumb-sm" role="img" aria-label="Lit tent at night" style="left:120px;top:186px;background:linear-gradient(160deg,#1b1b1b,#e0a040 60%,#2a2a2a)"></div>
    <div class="thumb thumb-sm" role="img" aria-label="Lion close-up" style="left:224px;top:186px;background:linear-gradient(160deg,#e0b47a,#9a6a3a)"></div>
    <div class="thumb thumb-sm" role="img" aria-label="Hiker in a canyon" style="left:328px;top:186px;background:linear-gradient(160deg,#6a3a2a,#2a1a16)"></div>
  </div>
  <h3 class="feat-title" style="left:100px">Detailed Outfitter Profiles</h3>
  <p class="feat-text" style="left:100px">Each outfitter in our directory has a dedicated profile page that provides in-depth information.</p>
  <h3 class="feat-title" style="left:641px">Booking System</h3>
  <p class="feat-text" style="left:641px">Booking system to make it easy for customers to book trips</p>
  <a class="btn btn-orange" style="left:641px;top:474px;width:132px;height:47px">Book Now</a>
</section>

<!-- CTA -->
<section class="cta">
  <svg class="abs" style="left:0;top:200px" width="1200" height="128" viewBox="0 0 1200 128">
    <path d="M0 60 C100 50 160 30 260 48 C360 28 460 30 560 50 C660 30 760 26 860 48 C960 30 1080 34 1200 52 L1200 84 L0 84 Z" fill="var(--sun-deep)"/>
  </svg>
  <h2 class="display">Interest in Joining Our Directory</h2>
  <p>The Online collaborative whiteboard platform to bring<br>team together , anytime, any where</p>
  <a class="btn" style="left:533px;top:188px;width:134px;height:45px;background:var(--orange-red)">Join Now</a>
  <div class="stripe" style="top:284px;height:15px;background:#f7941d"></div>
  <div class="stripe" style="top:299px;height:15px;background:var(--orange-red)"></div>
  <div class="stripe" style="top:314px;height:14px;background:var(--red)"></div>
</section>

<!-- CONTACT -->
<h2 class="section-title display" style="top:2740px">Get in Touch with Us</h2>
<div class="field" style="left:261px;top:2842px;width:345px">Name</div>
<div class="field" style="left:620px;top:2842px;width:346px">Email Id</div>
<div class="field" style="left:261px;top:2905px;width:345px">Phone</div>
<div class="field" style="left:620px;top:2905px;width:346px">Website</div>
<div class="field" style="left:261px;top:2968px;width:705px;height:107px">Message</div>
<div class="submit">Submit Now</div>

<!-- FOOTER -->
<footer class="footer">
  <div class="brand" style="left:100px;top:64px;font-size:14px"><span class="brand-dot" style="width:36px;height:36px"></span>Hiking Made Simple</div>
  <p class="abs" style="left:100px;top:152px;width:285px;font-size:12.5px;line-height:15.5px">Your go-to for outdoor tips, gear reviews, and adventures. Making nature your second home. Join the journey!</p>
  <div class="abs" style="left:100px;top:217px;font-family:'Oswald',sans-serif;font-weight:600;font-size:13px">FOLLOW US</div>
  <span class="social" style="left:100px"></span>
  <span class="social" style="left:134px;border-radius:6px"></span>
  <span class="social" style="left:168px"></span>
  <h4 class="foot-h" style="left:443px">Popular Collections</h4>
  <ul class="foot-list" style="left:443px"><li>Backpacks</li><li>Stoves</li><li>Camp Kitchen</li><li>Health &amp; Safety</li></ul>
  <h4 class="foot-h" style="left:669px">Customer Service</h4>
  <ul class="foot-list" style="left:669px"><li>Refund Policy</li><li>Privacy Policy</li><li>Terms of Service</li></ul>
  <h4 class="foot-h" style="left:870px">Keep in Touch</h4>
  <p class="abs" style="left:870px;top:101px;width:230px;font-size:12.5px;line-height:15.5px">Subscribe to our newsletter to receive updates on new products and exclusive subscriber-only offers.</p>
  <div class="abs" style="left:873px;top:177px;width:227px;height:34px;background:#fff"></div>
  <div class="abs" style="left:873px;top:220px;width:227px;height:34px;background:var(--orange);display:flex;align-items:center;justify-content:center;font-size:12px;font-weight:700">SUBMIT NOW</div>
  <div class="abs" style="left:0;top:333px;width:1200px;text-align:center;font-size:12.5px;font-weight:600">COPYRIGHT © 2012 - 2024 HIKING MADE SIMPLE ®. ALL RIGHTS RESERVED.</div>
</footer>

</body>
</html>
```